Aerial photo/video drone company needs new business card

Aerial visual company who offers photos and video services via drones.

We are QVL certified and work in the real estate, insurance, construction, and film industries.

I'm looking for a clean, professional, maybe even edgy design, that will be a conversation starter when networking.

I've included our logo, current business card, and font.

Our current business card is decent; albeit, I'm looking for something more unique. If you folks provide good designs, I'll definitely guarantee payment (and I'm not opposed to tipping if the design is above and beyond).

Target Market(s)

Insurance companies, real estate agents, construction companies, advertising & other creative agencies, and filmmakers/producers.

Industry/Entity Type

Business

Contact Information for Business Card

Company name pronounced air-a-vee.

Font styles to use
Other font styles liked:
• Font was uploaded; that or similar; not opposed to other fonts if they work well with the design

Requirements
Must have
• Clearly prominent logo; my name and title; phone number; email address; web address; mentioned "QVL Certified" or similar; should indicate "Aerial visual"
Nice to have
• Watermark of logo or otherwise
Should not have
• Pictures of drones or scenic shots

```html
<!DOCTYPE html>
<html lang="en">
<head>
<meta charset="utf-8">
<title>Skyvane Business Card</title>
<link rel="stylesheet" href="https://fonts.googleapis.com/css2?family=Montserrat:wght@500;600;700&family=Lato:wght@400&display=swap">
<style>
  :root {
    --backdrop: #e9e2d8;
    --card-white: #ffffff;
    --card-dark: #262b33;
    --navy: #1d3557;
    --sky: #1b8fd6;
    --ink: #3a3d42;
    --muted-light: #c9ccd1;
  }
  * { margin: 0; padding: 0; box-sizing: border-box; }
  html, body {
    width: 1200px; height: 801px; overflow: hidden;
    background: var(--backdrop);
    font-family: "Montserrat", sans-serif;
  }
  .canvas { position: relative; width: 1200px; height: 801px; }
  .card {
    position: absolute; width: 540px; height: 309px;
    border-radius: 4px;
    box-shadow: 0 10px 28px rgba(60, 45, 30, 0.18);
  }
  /* Back side */
  .card-back {
    left: 600px; top: 80px; background: var(--card-dark);
    display: flex; flex-direction: column; align-items: center; justify-content: center;
  }
  .back-brand { display: flex; align-items: center; gap: 14px; }
  .brand-dot { width: 26px; height: 26px; border-radius: 50%; background: var(--sky); }
  .back-brand .brand-name {
    font-weight: 600; font-size: 66px; letter-spacing: 1px; color: var(--muted-light); line-height: 1;
  }
  .back-tagline {
    margin-top: 18px; font-weight: 600; font-size: 13px; color: var(--sky); letter-spacing: .5px;
  }
  .back-industries {
    margin-top: 8px; font-weight: 600; font-size: 14px; color: var(--muted-light); letter-spacing: .5px;
  }
  .back-industries .sep { margin: 0 10px; }
  /* Front side */
  .card-front {
    left: 60px; top: 420px; background: var(--card-white);
    display: flex; align-items: center; padding: 0 40px 0 42px;
  }
  .front-brand { display: flex; align-items: center; gap: 12px; width: 250px; }
  .front-brand .brand-dot { width: 22px; height: 22px; }
  .front-brand .brand-name {
    font-weight: 600; font-size: 46px; color: var(--navy); line-height: 1;
  }
  .contact { margin-left: 26px; }
  .person-name { font-weight: 600; font-size: 22px; color: var(--ink); }
  .person-title { font-weight: 500; font-size: 15px; color: var(--sky); margin-top: 4px; letter-spacing: .5px; }
  .person-title .sep { margin: 0 6px; }
  .contact-list { list-style: none; margin-top: 14px; }
  .contact-list li {
    display: flex; align-items: center; gap: 10px;
    font-family: "Lato", sans-serif; font-size: 16px; color: var(--ink); margin-top: 5px;
  }
  .contact-list svg { width: 15px; height: 15px; fill: var(--sky); flex: none; }
</style>
</head>
<body>
<main class="canvas">
  <section class="card card-back" aria-label="Card back">
    <div class="back-brand">
      <span class="brand-dot"></span>
      <span class="brand-name">skyvane</span>
    </div>
    <p class="back-tagline">Aerial Visual for</p>
    <p class="back-industries">Real Estate<span class="sep">|</span>Insurance<span class="sep">|</span>Construction<span class="sep">|</span>Film</p>
  </section>

  <section class="card card-front" aria-label="Card front">
    <div class="front-brand">
      <span class="brand-dot"></span>
      <span class="brand-name">skyvane</span>
    </div>
    <div class="contact">
      <h1 class="person-name">Daniel T. Marlow</h1>
      <p class="person-title">Owner<span class="sep">|</span>sUAS Pilot</p>
      <ul class="contact-list">
        <li>
          <svg viewBox="0 0 16 16" aria-hidden="true"><path d="M1 3h14v10H1z M1 3l7 6 7-6" fill="none" stroke="#1b8fd6" stroke-width="1.6"/></svg>
          dan@skyvane.com
        </li>
        <li>
          <svg viewBox="0 0 16 16" aria-hidden="true"><path d="M2 6c0-2 2-3 6-3s6 1 6 3v1h-3V5.5H5V7H2z M4 8h8l2 6H2z"/></svg>
          555.014.2378
        </li>
        <li>
          <svg viewBox="0 0 16 16" aria-hidden="true"><g fill="none" stroke="#1b8fd6" stroke-width="1.3"><circle cx="8" cy="8" r="6.5"/><ellipse cx="8" cy="8" rx="3" ry="6.5"/><path d="M1.5 8h13M2.5 5h11M2.5 11h11"/></g></svg>
          skyvane.com
        </li>
      </ul>
    </div>
  </section>
</main>
</body>
</html>
```